Design my dad a new business card because his current one sucks!

I need a business card designed for my fathers home maintenance business. His customers are individuals (single moms, old people etc.) as well as the occasional business. As such it needs to be accessible to both target audiences.

The front of the card should be dark grey on yellow with the logo and contain the following information:
- Darren Whitlock
- 0488 372 915
- info@bluegumhomecare.example.au
- 0488 372 915

- ABN: 71 284 630 912
- 'Fully Insured'

The reverse should be yellow on dark grey and will have the web address:
- bluegumhomecare.example.au

And a few key services he offers:
GENERAL REPAIRS
PAINTING/TILING/
PAVING &CONCRETING
PRESSURE WASHING
ON-SITE WELDING
DECKING ADDITIONS & REPAIRS
FENCING
FULL BOND CLEANING

This will be first time the logo has been printed so you will need to come up with the best CMYK approximation of the RGB colours to make sure it is a close as possible.

```html
<!DOCTYPE html>
<html lang="en">
<head>
<meta charset="utf-8">
<title>Bluegum Home Care – Services Card</title>
<link rel="stylesheet" href="https://fonts.googleapis.com/css2?family=Carlito&display=swap">
<style>
  :root {
    --card-base: #626060;
    --card-light: #7a7978;
    --card-dark: #5a5858;
    --service-yellow: #ffff00;
    --web-white: #ffffff;
    --pointer-edge: #3a3a3a;
  }
  html, body {
    margin: 0;
    padding: 0;
    width: 1200px;
    height: 686px;
    overflow: hidden;
    background: var(--card-base);
  }
  .card-back {
    position: relative;
    width: 1200px;
    height: 686px;
    overflow: hidden;
    background:
      radial-gradient(ellipse 520px 620px at 560px 300px, var(--card-light) 0%, var(--card-base) 70%, var(--card-dark) 100%);
  }
  .card-back svg {
    display: block;
    position: absolute;
    inset: 0;
  }
  .service {
    font-family: "Carlito", "Calibri", sans-serif;
    font-size: 37px;
    fill: var(--service-yellow);
  }
  .web-address {
    font-family: "Carlito", "Calibri", sans-serif;
    font-size: 38px;
    fill: var(--web-white);
  }
  .pointer {
    fill: var(--web-white);
    stroke: var(--pointer-edge);
    stroke-width: 1.5;
    stroke-linejoin: round;
  }
</style>
</head>
<body>
  <main class="card-back">
    <svg width="1200" height="686" viewBox="0 0 1200 686" aria-label="Services offered">
      <g class="service-list">
        <text class="service" x="58" y="160">GENERAL REPAIRS</text>
        <text class="service" x="484" y="160">FULL BOND CLEANING</text>
        <text class="service" x="1137" y="160" text-anchor="end">TILING</text>

        <text class="service" x="58" y="303">PAVING &amp;CONCRETING</text>
        <text class="service" x="543" y="303">PRESSURE WASHING</text>
        <text class="service" x="1135" y="303" text-anchor="end">FENCING</text>

        <text class="service" x="130" y="445">ON-SITE WELDING</text>
        <text class="service" x="519" y="445">DECKING ADDITIONS &amp; REPAIRS</text>

        <text class="service" x="519" y="586">PAINTING</text>
      </g>

      <text class="web-address" x="916" y="668" text-anchor="end">bluegumhomecare.example.au</text>

      <path class="pointer" d="M929 645 L929 669 L935 663 L940 674 L944 672 L939 661 L947 661 Z"/>
    </svg>
  </main>
</body>
</html>
```